Letterhead Design Project

We have recently updated our corporate logo and are seeking a new letterhead template.

Attached is the new logo and the old letterhead.

PLEASE DO NOT USE OUR EXISTING WEB SITE FOR INSPIRATION as we are redesigning it.

Target Market(s)

Executives, search professionals, technical and scientific professionals

Industry/Entity Type

Seeking

```html
<!DOCTYPE html>
<html lang="en">
<head>
<meta charset="utf-8">
<title>HelixScope Letterhead</title>
<link rel="stylesheet" href="https://fonts.googleapis.com/css2?family=Arimo:wght@400;700&display=swap">
<style>
  :root {
    --paper: #ffffff;
    --band: #ddeef7;
    --watermark: #e8f3fa;
    --brand-blue: #2a93c9;
    --text-grey: #6e6e6e;
  }
  * { margin: 0; padding: 0; box-sizing: border-box; }
  html, body {
    width: 848px;
    height: 1200px;
    overflow: hidden;
    background: var(--paper);
  }
  .letterhead {
    position: relative;
    width: 848px;
    height: 1200px;
    background: var(--paper);
    font-family: "Arimo", Arial, sans-serif;
  }
  .header-band {
    position: absolute;
    left: 230px;
    top: 0;
    width: 388px;
    height: 135px;
    background: var(--band);
    display: flex;
    align-items: center;
    justify-content: center;
    gap: 10px;
  }
  .brand-dot {
    width: 44px;
    height: 44px;
    border-radius: 50%;
    background: var(--brand-blue);
  }
  .brand-name {
    font-weight: 700;
    font-size: 34px;
    letter-spacing: -0.5px;
    color: var(--brand-blue);
  }
  .watermark-disc {
    position: absolute;
    left: 234px;
    top: 620px;
    width: 384px;
    height: 384px;
    border-radius: 50%;
    background: var(--watermark);
  }
  .footer-band {
    position: absolute;
    left: 230px;
    top: 1064px;
    width: 388px;
    height: 136px;
    background: var(--band);
    padding-top: 21px;
    text-align: center;
    font-size: 13px;
    line-height: 20.5px;
    color: var(--text-grey);
  }
  .footer-band .web {
    color: var(--brand-blue);
    font-weight: 700;
  }
</style>
</head>
<body>
  <div class="letterhead">
    <header class="header-band">
      <span class="brand-dot" aria-hidden="true"></span>
      <span class="brand-name">HelixScope</span>
    </header>

    <div class="watermark-disc" aria-hidden="true"></div>

    <footer class="footer-band">
      <p>voice 555.214.0100, fax 555.214.0100</p>
      <p>2200 Harbor Point Road, Suite 140, Easton, MA 02375</p>
      <p class="web">www.helixscope.com</p>
    </footer>
  </div>
</body>
</html>
```